Kick Ass, Edgy, Fun, E commerce Embroidery Company Business Card

Sleek and edgy business card layout. main logo on front with business description (Custom Embroidery, the file is submitted is supposed to look like stitching)
Name, address, phone numbers, social icons (Facebook and Instagram) on back. The card will be black plastic and the front main logo will be printed Spot UV.

Target Market(s)

Small Business Owners

Contact Information for Business Card

Focused, not cluttered and sleek. Modern looking.

Font styles to use
Other font styles liked:
• Very clean and elegant

Colors
acd136

Requirements
Must have
• Custom Embroidery

our Tagline: Every Logo Has A Story - Thread Yours
Nice to have
• Social Icons for Facebook and Instagram
Should not have
• Too much visual noise

```html
<!DOCTYPE html>
<html lang="en">
<head>
<meta charset="utf-8">
<title>StitchRally Business Card</title>
<link rel="stylesheet" href="https://fonts.googleapis.com/css2?family=Arimo:wght@400;700&family=Signika:wght@600&display=swap">
<style>
  :root {
    --lime: #acd136;
    --stage: #a2c125;
    --ink: #000000;
    --paper: #ffffff;
  }
  * { box-sizing: border-box; margin: 0; padding: 0; }
  html, body { width: 1200px; height: 1200px; overflow: hidden; }
  body {
    position: relative;
    background: var(--stage);
    font-family: "Arimo", Arial, sans-serif;
  }
  .card {
    position: absolute;
    left: 311px;
    width: 585px;
    height: 366px;
    border-radius: 26px;
    overflow: hidden;
  }
  .card--front { top: 186px; background: var(--paper); }
  .card--back { top: 649px; background: var(--ink); color: var(--paper); }

  /* Front */
  .brand-mark {
    position: absolute;
    left: 0; right: 0;
    top: 320px;
    display: flex;
    align-items: center;
    justify-content: center;
    gap: 14px;
  }
  .front-name {
    position: absolute;
    left: 0; right: 0; top: 146px;
    display: flex; align-items: center; justify-content: center; gap: 14px;
    font-weight: 700;
    font-size: 46px;
    letter-spacing: 1px;
    color: var(--ink);
  }
  .name-dot {
    width: 40px; height: 40px; border-radius: 50%;
    background: var(--lime);
  }
  .tagline-band {
    position: absolute;
    left: 0; right: 0; top: 301px;
    height: 17px;
  }
  .band-bar { position: absolute; top: 0; height: 17px; }
  .band-bar--ink { left: 0; width: 119px; background: var(--ink); }
  .band-bar--lime { right: 0; width: 121px; background: var(--lime); }
  .tagline {
    position: absolute;
    left: 127px; width: 330px; top: -4px;
    font-family: "Signika", "Trebuchet MS", sans-serif;
    font-weight: 600;
    font-size: 18.5px;
    line-height: 24px;
    white-space: nowrap;
    color: var(--ink);
  }
  .tagline em { font-style: normal; color: var(--lime); }

  /* Back */
  .side-bar {
    position: absolute; top: 101px; height: 160px;
    background: var(--lime);
  }
  .side-bar--left { left: 1px; width: 12px; }
  .side-bar--right { right: 0; width: 9px; }
  .back-brand {
    position: absolute;
    left: 110px; width: 180px; top: 118px;
    text-align: center;
  }
  .back-brand .name-dot { width: 64px; height: 64px; background: var(--paper); margin: 0 auto 16px; }
  .back-name {
    font-weight: 700; font-size: 30px; line-height: 28px;
    color: var(--paper); letter-spacing: 1px;
  }
  .divider {
    position: absolute; left: 292px; top: 101px;
    width: 2px; height: 160px; background: var(--paper);
  }
  .details { position: absolute; left: 306px; top: 104px; }
  .company { color: var(--lime); font-weight: 700; font-size: 25px; line-height: 30px; }
  .address { font-size: 16.5px; line-height: 23px; margin-top: 1px; }
  .contacts { list-style: none; margin-top: 18px; }
  .contacts li {
    display: flex; align-items: center; gap: 7px;
    font-size: 17px; line-height: 22.5px; letter-spacing: 0.3px;
  }
  .contacts svg { width: 14px; height: 14px; flex: none; }
  .socials { display: flex; gap: 19px; margin-top: 24px; margin-left: 4px; }
  .social {
    width: 26px; height: 24px;
    border: 1.5px solid var(--lime);
    border-radius: 6px;
  }
</style>
</head>
<body>
  <section class="card card--front">
    <div class="front-name"><span class="name-dot"></span>STITCH RALLY</div>
    <div class="tagline-band">
      <span class="band-bar band-bar--ink"></span>
      <p class="tagline">Every Logo Has A Story - <em>Thread Yours!</em></p>
      <span class="band-bar band-bar--lime"></span>
    </div>
  </section>

  <section class="card card--back">
    <span class="side-bar side-bar--left"></span>
    <span class="side-bar side-bar--right"></span>
    <div class="back-brand">
      <div class="name-dot"></div>
      <div class="back-name">STITCH<br>RALLY</div>
    </div>
    <span class="divider"></span>
    <div class="details">
      <h1 class="company">StitchRally Inc</h1>
      <p class="address">417 Loomis Ridge Dr Ste 5<br>Brookfield, CO 80344</p>
      <ul class="contacts">
        <li>
          <svg viewBox="0 0 14 14" aria-hidden="true"><rect x="3.5" y="1" width="7" height="12" rx="1.2" fill="none" stroke="#acd136" stroke-width="1.4"/><circle cx="7" cy="11" r="0.8" fill="#acd136"/></svg>
          1-800-555-0148
        </li>
        <li>
          <svg viewBox="0 0 14 14" aria-hidden="true"><rect x="0.8" y="3" width="12.4" height="8.5" fill="#acd136"/><path d="M1 3.3 L7 8 L13 3.3" fill="none" stroke="#000" stroke-width="1"/></svg>
          info@StitchRally.com
        </li>
        <li>
          <svg viewBox="0 0 14 14" aria-hidden="true"><g fill="none" stroke="#acd136" stroke-width="1.1"><circle cx="7" cy="7" r="5.8"/><ellipse cx="7" cy="7" rx="2.6" ry="5.8"/><path d="M1.2 7h11.6M2 4h10M2 10h10"/></g></svg>
          StitchRally.com
        </li>
      </ul>
      <div class="socials">
        <span class="social" aria-label="Social profile"></span>
        <span class="social" aria-label="Social profile"></span>
      </div>
    </div>
  </section>
</body>
</html>
```